Newsletter Banner Ad with a URL to our website offering

We need a banner ad for a newsletter that is published to members biweekly that simply articulates our value proposition and enables the reader to click on our logo to learn more and engage with us to schedule an Emergency Response Plan so they are ready for when a burst pipe happens on their property. They will have a plan after they engage with us.
We need quotes to build two options 1&2

```html
<!DOCTYPE html>
<html lang="en">
<head>
<meta charset="utf-8">
<title>Brightway Property Restoration – Newsletter Banner</title>
<link rel="stylesheet" href="https://fonts.googleapis.com/css2?family=Montserrat:wght@500;800&family=Oswald:wght@600;700&display=swap">
<style>
  :root {
    --stage: #555555;
    --red: #e8161b;
    --red-deep: #c80d14;
    --red-light: #f0262a;
    --navy: #0f1d57;
    --white: #ffffff;
    --spray-light: #f1f1f1;
    --spray-mid: #cfc9c2;
    --pipe-red: #b0303c;
  }
  * { margin: 0; padding: 0; box-sizing: border-box; }
  html, body {
    width: 1200px; height: 600px; overflow: hidden;
    background: var(--stage);
  }
  .banner {
    position: absolute;
    left: 61px; top: 159px;
    width: 1077px; height: 277px;
    overflow: hidden;
    background:
      linear-gradient(180deg, var(--red-light) 0%, var(--red-light) 23%, var(--red-deep) 24%, var(--red) 60%, var(--red-deep) 100%);
  }
  .city-backdrop {
    position: absolute; inset: 0;
    background: linear-gradient(90deg, rgba(180,8,14,0.15), rgba(255,40,40,0.05) 60%, rgba(180,8,14,0.2));
  }
  .graphics {
    position: absolute; inset: 0;
    width: 1077px; height: 277px;
  }
  .brand {
    position: absolute; left: 225px; top: 20px;
    display: flex; align-items: center; gap: 10px;
    color: var(--white);
    font-family: "Oswald", sans-serif; font-weight: 700;
  }
  .brand-dot {
    width: 44px; height: 44px; border-radius: 50%;
    background: var(--white);
  }
  .brand-name {
    display: flex; flex-direction: column; line-height: 1;
  }
  .brand-name .main { font-size: 29px; letter-spacing: 3.5px; }
  .brand-name .sub { font-size: 11.5px; letter-spacing: 2.2px; margin-top: 3px; }
  .headline {
    position: absolute; left: 23px; top: 72px;
    color: var(--white);
    font-family: "Montserrat", sans-serif;
  }
  .headline .lead, .headline .tail {
    display: block; font-weight: 500; font-size: 35px; letter-spacing: -1px; line-height: 48px;
  }
  .headline .key {
    display: block; font-weight: 800; font-size: 41px; letter-spacing: -1px; line-height: 50px;
  }
  .cta-call {
    position: absolute; left: 28px; top: 226px;
    width: 219px; height: 32px;
    display: flex; align-items: center;
  }
  .cta-call .plate {
    position: absolute; inset: 0;
    background: var(--navy);
    transform: skewX(-12deg);
  }
  .icon {
    position: relative;
    width: 20px; height: 20px; border-radius: 50%;
    display: flex; align-items: center; justify-content: center;
    flex-shrink: 0;
  }
  .cta-call .icon { background: var(--red); margin-left: 15px; }
  .cta-web .icon { background: var(--white); }
  .cta-label {
    position: relative;
    color: var(--white);
    font-family: "Oswald", sans-serif; font-weight: 600;
    font-size: 15.5px; letter-spacing: 0.2px;
    margin-left: 8px;
  }
  .cta-web {
    position: absolute; left: 276px; top: 232px;
    display: flex; align-items: center;
  }
  .cta-web .cta-label { margin-left: 6px; }
</style>
</head>
<body>
  <section class="banner" aria-label="Brightway Property Restoration banner">
    <div class="city-backdrop" role="img" aria-label="Red-tinted aerial photo of a city skyline"></div>

    <svg class="graphics" viewBox="0 0 1077 277" aria-hidden="false">
      <defs>
        <radialGradient id="sprayTone" cx="0.55" cy="0.55" r="0.7">
          <stop offset="0" stop-color="var(--spray-light)"/>
          <stop offset="0.7" stop-color="#e4e2df"/>
          <stop offset="1" stop-color="var(--spray-mid)"/>
        </radialGradient>
      </defs>
      <polygon class="photo-area" points="704.8,0 1058.8,0 980.5,277 625.6,277" fill="url(#sprayTone)" role="img" aria-label="Photo of a red fire sprinkler head bursting and spraying water"/>
      <polygon class="stripe-left" points="660.5,0 704.8,0 625.6,277 581.3,277" fill="var(--navy)"/>
      <polygon class="stripe-right" points="1058.8,0 1077,0 1077,277 980.5,277" fill="var(--navy)"/>
      <polygon class="corner-red" points="1023.8,277 1077,277 1077,150 1060,150" fill="var(--red-deep)"/>
      <line class="accent-line" x1="632.6" y1="141" x2="602.3" y2="277" stroke="var(--white)" stroke-width="1.6"/>
      <line class="accent-line" x1="1068" y1="10.7" x2="1051.8" y2="122.5" stroke="var(--white)" stroke-width="1.6"/>
    </svg>

    <div class="brand">
      <span class="brand-dot"></span>
      <span class="brand-name">
        <span class="main">BRIGHTWAY</span>
        <span class="sub">PROPERTY RESTORATION</span>
      </span>
    </div>

    <h1 class="headline">
      <span class="lead">Do you have a</span>
      <span class="key">RAPID RESPONSE PLAN</span>
      <span class="tail">for this?</span>
    </h1>

    <div class="cta-call">
      <span class="plate"></span>
      <span class="icon">
        <svg width="11" height="11" viewBox="0 0 24 24"><path fill="#fff" d="M6.6 10.8a15.1 15.1 0 0 0 6.6 6.6l2.2-2.2c.3-.3.7-.4 1-.2 1.1.4 2.3.6 3.6.6.6 0 1 .4 1 1V20c0 .6-.4 1-1 1C10.6 21 3 13.4 3 4c0-.6.4-1 1-1h3.5c.6 0 1 .4 1 1 0 1.2.2 2.4.6 3.6.1.3 0 .7-.2 1z"/></svg>
      </span>
      <span class="cta-label">CALL NOW! (888) 555-0142</span>
    </div>

    <div class="cta-web">
      <span class="icon">
        <svg width="13" height="13" viewBox="0 0 24 24" fill="none" stroke="var(--red)" stroke-width="2.2"><circle cx="12" cy="12" r="9"/><ellipse cx="12" cy="12" rx="4" ry="9"/><line x1="3" y1="12" x2="21" y2="12"/></svg>
      </span>
      <span class="cta-label">WWW.CALLBRIGHTWAY.COM</span>
    </div>
  </section>
</body>
</html>
```